Design blogshop facebook and logo

Design logo and blog shop facebook design.
Reference https://www.pagenook.com/Belmi-Trendora-527316904182635/?ref=ts&fref=ts
Want a more trendy elegant and fashionable design for the logo and facebook

Industry/Entity Type

Shop

Colors
ffffff
ec1f27
f68d4d

```html
<!DOCTYPE html>
<html lang="en">
<head>
<meta charset="utf-8">
<title>Belmi Trendora – Facebook Cover &amp; Profile Set</title>
<link href="https://fonts.googleapis.com/css2?family=Cinzel:wght@400&family=Questrial&family=Arimo&display=swap" rel="stylesheet">
<style>
  :root{
    --board:#ffffff;
    --frame:#2b2b2b;
    --ink:#1c1c1c;
    --panel-dark:#1d1d1d;
    --gold:#c9a24a;
    --red:#ec1f27;
    --orange:#f68d4d;
    --text-dark:#2a2a2a;
    --title-faint:#3e3e3e;
    --light:#ffffff;
  }
  *{box-sizing:border-box;margin:0;padding:0}
  html,body{width:1200px;height:1200px;overflow:hidden;background:var(--board)}
  .board{position:relative;width:1200px;height:1200px;border:2px solid var(--frame);background:var(--board)}
  .abs{position:absolute}

  /* cover 1 – light */
  .cover-light{left:169px;top:107px;width:852px;height:316px;border:1px solid #b9b9b9;
    background:linear-gradient(90deg,#d9d9db 0%,#ececee 30%,#e4e4e6 55%,#eeeeef 100%);overflow:hidden}
  .cover-light .hero-photo{left:230px;top:55px;width:240px;height:262px;border-radius:110px 110px 0 0;
    background:linear-gradient(180deg,#2a2a2e 0%,#3a3335 35%,#c9a894 60%,#1e1e1e 100%)}
  .thumb{background:linear-gradient(180deg,#d8d6d4 0%,#bdb9b6 45%,#4a4a4a 70%,#dcdcdc 100%)}
  .brand-small{display:flex;align-items:center;gap:8px;font-family:"Cinzel",serif;font-size:19px;color:var(--text-dark);letter-spacing:.5px}
  .brand-small .dot{width:24px;height:24px;border:2px solid var(--red);border-radius:50%}
  .tagline{font-family:"Questrial",sans-serif;line-height:1.3}
  .cover-light .tagline{left:516px;top:188px;width:330px;font-size:17px;color:var(--text-dark)}

  /* profile squares */
  .profile{width:180px;height:180px;display:flex;flex-direction:column;align-items:center;justify-content:center;gap:14px}
  .profile.dark{background:var(--panel-dark)}
  .profile.white{background:var(--light);border:1px solid #bdbdbd}
  .profile .mark{width:96px;height:96px;border-radius:50%;border:4px solid var(--gold)}
  .profile.white .mark{border-color:var(--red)}
  .profile .name{font-family:"Cinzel",serif;font-size:17px;color:var(--gold);letter-spacing:.5px}
  .profile.white .name{color:var(--text-dark)}

  /* cover 2 – dark */
  .cover-dark{left:163px;top:531px;width:852px;height:316px;background:var(--panel-dark);border:1px solid #555;overflow:hidden}
  .cover-dark .title{left:468px;top:118px;font-family:"Cinzel",serif;font-size:30px;color:var(--title-faint);letter-spacing:.5px}
  .cover-dark .tagline{left:468px;top:158px;width:370px;font-size:19.5px;color:var(--light)}

  .caption{left:769px;top:1145px;font-family:"Arimo",sans-serif;font-size:28px;color:var(--ink)}
</style>
</head>
<body>
<main class="board">

  <section class="cover-light abs" aria-label="Facebook cover, light version">
    <div class="hero-photo abs" role="img" aria-label="Portrait photo of a smiling model with sunglasses on her head in front of a white curtain"></div>
    <div class="thumb abs" style="left:462px;top:9px;width:116px;height:116px" role="img" aria-label="Outfit photo: striped top with red bag"></div>
    <div class="thumb abs" style="left:588px;top:9px;width:116px;height:116px" role="img" aria-label="Outfit photo: black and white striped top"></div>
    <div class="thumb abs" style="left:716px;top:9px;width:116px;height:116px;background:linear-gradient(180deg,#d8d6d4 0%,#2a2a2a 45%,#8a8a8a 70%,#1e1e1e 100%)" role="img" aria-label="Outfit photo: embellished top on a black sofa"></div>
    <div class="brand-small abs" style="left:513px;top:143px"><span class="dot"></span>BELMI TRENDORA</div>
    <p class="tagline abs">Belmi Trendora the world of stylish fashion for all sophisticated women on earth!!</p>
  </section>

  <div class="profile dark abs" style="left:222px;top:327px">
    <span class="mark"></span><span class="name">BELMI TRENDORA</span>
  </div>

  <section class="cover-dark abs" aria-label="Facebook cover, dark version">
    <div class="thumb abs" style="left:473px;top:40px;width:72px;height:71px" role="img" aria-label="Outfit photo: striped top with red bag"></div>
    <div class="thumb abs" style="left:551px;top:40px;width:72px;height:71px" role="img" aria-label="Outfit photo: black and white striped top"></div>
    <div class="thumb abs" style="left:629px;top:40px;width:72px;height:71px;background:linear-gradient(180deg,#d8d6d4 0%,#2a2a2a 45%,#8a8a8a 70%,#1e1e1e 100%)" role="img" aria-label="Outfit photo: embellished top on a black sofa"></div>
    <h2 class="title abs">BELMI TRENDORA</h2>
    <p class="tagline abs">Belmi Trendora the world of stylish fashion for all sophisticated women on earth!!</p>
  </section>

  <div class="profile dark abs" style="left:218px;top:727px">
    <span class="mark"></span><span class="name">BELMI TRENDORA</span>
  </div>

  <div class="profile dark abs" style="left:642px;top:944px">
    <span class="mark"></span><span class="name">BELMI TRENDORA</span>
  </div>
  <div class="profile white abs" style="left:834px;top:941px">
    <span class="mark"></span><span class="name">BELMI TRENDORA</span>
  </div>

  <p class="caption abs">Profile Pic</p>
</main>
</body>
</html>
```